Give Bright Oak an Online Presence!

Bright Oak Property Maintenance is an Australian Owned property maintenance company who needs a stand out online presence.

BOK maintains many buildings and sites and wants to appeal to a corporate professional market with their brand new website. BOK is essentially a handyman service offering all maintenance services to home owners, office managers, real estate agents and strata managers.

The Website:
We need a corporate website that appeals to our broader customer base (property owners, property managers, office managers) the copy is being written by a professional so use filler text for now.

Things that we want:
Home page that sets us apart and appeals to the corporate and residential market. The home page needs to not focus on either the residential or commercial market. The home page should focus on our logo and branding. We have a logo already and it is attached to the brief, please use it and try to consider the colour pallette that goes with it. Whilst we want the site to appear strong and manly it is important to remember that 95% of our customers are female so we need the site to be appealing to women. Women need to believe that we are strong, dependable and trustworthy.
We'd like a quote page and potentially also the ability to get a quote from the home page (please don't put it in if it ruins the overall feel of the home page)
An "about us" page
A contact us page
A blog that's built in (we don't want to link to an external blog)
(overall we'd expect to have 6 or 7 pages total)

The site will also need coding - we expect this to be done in a separate project but need you to consider a few things about the coding side of things.

It needs to be iPhone and iPad compatible.

We'd like you to suggest the best CMS that you would use or if you would suggest not using a CMS please let us know with your submissions.

Target Market(s)

Property owners, office managers and property managers who need maintenance on buildings (So all of them)

Industry/Entity Type

Property Maintenance

Requirements
Must have
• Our Logo
Home page
About Us
Residential
Commercial
Real Estate/Strata
Contact Us/Quote
Blog
Nice to have
• Quote form included in home page
Movement on the home page at least
Should not have
• other logos, too much colour
NO FLASH

```html
<!DOCTYPE html>
<html lang="en">
<head>
<meta charset="utf-8">
<title>Bright Oak Property Maintenance</title>
<link rel="stylesheet" href="https://fonts.googleapis.com/css2?family=Arimo:wght@400;700&family=Raleway:wght@300;700&family=Roboto+Condensed:ital,wght@0,400;0,700;1,400;1,500&display=swap">
<style>
  :root {
    --orange: #f07a12;
    --orange-deep: #e8560a;
    --orange-light: #f9a21e;
    --glow: #fbc02a;
    --ink: #141210;
    --bar-top: #3a3a3a;
    --bar-bottom: #0c0c0c;
    --text: #4a4a4a;
    --text-soft: #5a5a5a;
    --rule: #d9d9d9;
    --white: #ffffff;
    --page: #ffffff;
    --page-edge: #e4e4e4;
  }
  * { margin: 0; padding: 0; box-sizing: border-box; }
  html, body { width: 1200px; height: 1196px; overflow: hidden; }
  body {
    position: relative;
    background: var(--page);
    font-family: "Arimo", Arial, sans-serif;
    color: var(--text);
  }

  /* Top navigation */
  .top-bar {
    position: absolute; left: 0; top: 0; width: 1200px; height: 46px;
    background: linear-gradient(var(--bar-top), var(--bar-bottom));
  }
  .main-nav { position: absolute; left: 125px; top: 0; height: 46px; display: flex; }
  .main-nav a {
    display: flex; align-items: center; justify-content: center;
    height: 46px; color: var(--white); text-decoration: none;
    font-family: "Roboto Condensed", sans-serif; font-weight: 700; font-size: 11px;
    border-left: 1px solid #2c2c2c; border-right: 1px solid #000;
  }
  .search {
    position: absolute; left: 918px; top: 10px; width: 187px; height: 24px;
    border-radius: 5px; background: #1c1c1c; border: 1px solid #4a4a4a;
    box-shadow: inset 0 1px 3px #000;
  }
  .search svg { position: absolute; left: 12px; top: 4px; }
  .search span {
    position: absolute; right: 22px; top: 5px; font-size: 10px; color: #8a8a8a;
  }

  /* Hero */
  .hero {
    position: absolute; left: 0; top: 46px; width: 1200px; height: 372px; overflow: hidden;
    background:
      radial-gradient(circle at 240px 170px, var(--glow) 0, var(--orange-light) 150px, rgba(249,162,30,0) 330px),
      linear-gradient(180deg, var(--orange-deep) 0%, var(--orange) 45%, var(--orange-light) 100%);
  }
  .skyline {
    position: absolute; left: 0; bottom: 0; width: 1200px; height: 130px;
    background: linear-gradient(180deg, rgba(20,18,16,0) 0%, rgba(20,18,16,0.55) 45%, var(--ink) 80%);
  }
  .brand-name {
    position: absolute; left: 118px; top: 218px; width: 250px; text-align: center;
    font-family: "Raleway", sans-serif; font-weight: 700; font-size: 26px; line-height: 30px;
    color: var(--white);
  }
  .brand-name small { display: block; font-size: 16px; line-height: 20px; }
  .hero-title {
    position: absolute; left: 453px; top: 60px;
    font-family: "Raleway", sans-serif; font-weight: 700; font-size: 31px; letter-spacing: -1px;
    color: var(--white);
  }
  .hero-intro {
    position: absolute; left: 453px; top: 126px; width: 420px;
    font-family: "Raleway", sans-serif; font-weight: 300; font-size: 21px; line-height: 29px;
    color: var(--white);
  }

  /* Content */
  .content-area {
    position: absolute; left: 0; top: 418px; width: 1200px; height: 665px;
    background: linear-gradient(180deg, var(--page-edge) 0, var(--page) 50px, var(--page) 610px, var(--page-edge) 665px);
    border-top: 2px solid #d0d0d0;
  }
  .section-title {
    position: absolute; font-family: "Roboto Condensed", sans-serif; font-style: italic;
    font-weight: 500; font-size: 19px; color: #555;
  }
  .section-title em { color: var(--orange-light); font-style: italic; }
  .dotted { position: absolute; border-top: 1px dotted #c4c4c4; height: 0; }
  .divider-v { position: absolute; left: 754px; top: 489px; height: 544px; border-left: 1px dotted #c4c4c4; }

  .post { position: absolute; left: 130px; width: 584px; }
  .post-title { position: absolute; left: 0; top: 0; font-size: 16px; font-weight: 400; color: #4a4a4a; letter-spacing: .3px; }
  .post-meta { position: absolute; right: 0; top: 3px; font-size: 10.5px; color: #555; }
  .post-meta a { color: var(--orange); text-decoration: none; }
  .post-photo {
    position: absolute; left: 0; width: 160px; height: 166px;
    box-shadow: 0 2px 3px rgba(0,0,0,.35);
  }
  .post-photo.tool { background: linear-gradient(135deg, #b9b4ae, #6f6a64 55%, #a36b3d); }
  .post-photo.window { background: linear-gradient(135deg, #d9d2b2, #7a9a58 50%, #c9cfd6); }
  .post-body { position: absolute; left: 187px; width: 410px; font-size: 11.5px; line-height: 14.5px; color: var(--text-soft); }
  .post-body p + p { margin-top: 17px; }
  .pill {
    position: absolute; display: flex; align-items: center; justify-content: center;
    height: 23px; border-radius: 12px; font-size: 11px; color: var(--white); text-decoration: none;
    background: linear-gradient(var(--orange-light), var(--orange-deep));
  }
  .pill.dark { background: linear-gradient(#3a3a3a, #0c0c0c); }
  .read-more { left: 187px; width: 70px; }
  .post-rule { position: absolute; left: 134px; top: 778px; width: 588px; border-top: 1px solid #e3e3e3; }

  .categories { position: absolute; left: 832px; top: 507px; width: 226px; list-style: none; }
  .categories li {
    height: 37px; border-bottom: 1px solid var(--rule); display: flex; align-items: center;
    padding-left: 7px; font-size: 12px; font-weight: 700; color: var(--text-soft); letter-spacing: 1px;
  }
  .categories svg { margin-right: 10px; }

  .contact-info { position: absolute; left: 834px; top: 834px; font-size: 12px; font-weight: 700; line-height: 14.5px; color: var(--text-soft); letter-spacing: 1px; font-style: normal; }
  .contact-info p + p { margin-top: 13px; }

  /* Footer */
  .footer {
    position: absolute; left: 0; top: 1083px; width: 1200px; height: 113px;
    background: linear-gradient(#2e2e2e, #0e0e0e 70%, #161616);
    border-top: 3px solid #f4f4f4;
  }
  .footer-nav { position: absolute; top: 22px; left: 0; width: 1200px; height: 30px; }
  .footer-nav a {
    position: absolute; top: 9px; font-size: 10px; letter-spacing: 1px; color: var(--white); text-decoration: none;
  }
  .footer-nav i { position: absolute; top: 0; height: 30px; border-left: 1px solid #444; }
</style>
</head>
<body>
  <header class="top-bar">
    <nav class="main-nav">
      <a href="#" style="width:94px">HOME</a>
      <a href="#" style="width:115px">ABOUT US</a>
      <a href="#" style="width:125px">RESIDENTIAL</a>
      <a href="#" style="width:114px">COMMERCIAL</a>
      <a href="#" style="width:118px">REAL ESTATE</a>
      <a href="#" style="width:116px">CONTACT US</a>
    </nav>
    <div class="search">
      <svg width="16" height="16" viewBox="0 0 16 16"><circle cx="9.5" cy="6.5" r="4.5" fill="#cfe3f5" stroke="#9ab" stroke-width="1.2"/><line x1="6" y1="10" x2="2" y2="14" stroke="#d48b2a" stroke-width="2.4" stroke-linecap="round"/></svg>
      <span>search...</span>
    </div>
  </header>

  <section class="hero">
    <div class="skyline" role="img" aria-label="City skyline silhouette along the bottom of the banner"></div>
    <div class="brand-name">Bright Oak<small>Property Maintenance</small></div>
    <h1 class="hero-title">We are Bright Oak</h1>
    <p class="hero-intro">Our goal is to connect people in search of quality property maintenance both for residential and commercial clients.</p>
  </section>

  <main class="content-area"></main>

  <h2 class="section-title" style="left:130px;top:453px">Latest <em>Posts</em></h2>
  <div class="dotted" style="left:130px;top:489px;width:467px"></div>
  <div class="divider-v"></div>

  <article class="post" style="top:522px">
    <h3 class="post-title">Working out the maintanence plan</h3>
    <div class="post-meta">Posted on 22th December, in <a href="#">Electrics &amp; Plumbing</a></div>
    <div class="post-photo tool" style="top:50px" role="img" aria-label="Tradesman cutting timber with a power jigsaw"></div>
    <div class="post-body" style="top:60px">
      <p>Lorem ipsum dolor sit amet, pri ei illud etiam latine. Ne has inimicus praesent persequeris, at apeirian disputando intellegebat his. Ad saepe integre menandri eum, choro tincidunt eos ut. Eam elit mandamus id, ne his sonet dicunt.</p>
      <p>Ad saepe integre menandri eum, choro tincidunt eos ut. Eam elit manda-mus id, ne his sonet dicunt.</p>
    </div>
    <a class="pill read-more" href="#" style="top:183px">read more</a>
  </article>

  <div class="post-rule"></div>

  <article class="post" style="top:817px">
    <h3 class="post-title">Working out the maintanence plan</h3>
    <div class="post-meta">Posted on 22th December, in <a href="#">Electrics &amp; Plumbing</a></div>
    <div class="post-photo window" style="top:48px;height:164px" role="img" aria-label="Hand wiping a window pane with a cloth"></div>
    <div class="post-body" style="top:58px">
      <p>Lorem ipsum dolor sit amet, pri ei illud etiam latine. Ne has inimicus praesent persequeris, at apeirian disputando intellegebat his.</p>
      <p>Ne has inimicus praesent persequeris, at apeirian disputando intellegebat his. Ad saepe integre menandri eum, choro tincidunt eos ut. Eam elit man-damus id, ne his sonet dicunt.</p>
    </div>
    <a class="pill read-more" href="#" style="top:188px">read more</a>
  </article>

  <aside>
    <h2 class="section-title" style="left:834px;top:449px">Categories</h2>
    <div class="dotted" style="left:832px;top:489px;width:226px"></div>
    <ul class="categories">
      <li><svg width="6" height="9" viewBox="0 0 6 9"><path d="M0.5 0.5 L5.5 4.5 L0.5 8.5 Z" fill="none" stroke="#666"/></svg>Spring house cleaning (2)</li>
      <li><svg width="6" height="9" viewBox="0 0 6 9"><path d="M0.5 0.5 L5.5 4.5 L0.5 8.5 Z" fill="none" stroke="#666"/></svg>Know how to repair lights (3)</li>
      <li><svg width="6" height="9" viewBox="0 0 6 9"><path d="M0.5 0.5 L5.5 4.5 L0.5 8.5 Z" fill="none" stroke="#666"/></svg>Electrics &amp; Plumbing (7)</li>
      <li><svg width="6" height="9" viewBox="0 0 6 9"><path d="M0.5 0.5 L5.5 4.5 L0.5 8.5 Z" fill="none" stroke="#666"/></svg>Lawn mowing (1)</li>
      <li><svg width="6" height="9" viewBox="0 0 6 9"><path d="M0.5 0.5 L5.5 4.5 L0.5 8.5 Z" fill="none" stroke="#666"/></svg>Do it yourself (9)</li>
    </ul>

    <h2 class="section-title" style="left:834px;top:760px">Contact <em>Us</em></h2>
    <div class="dotted" style="left:832px;top:802px;width:226px"></div>
    <address class="contact-info">
      <p>City Name, Australia<br>42-44 Harbour Lane<br>Central, Sydney</p>
      <p>bok@info.com</p>
      <p>0800 417562<br>0800 417580</p>
    </address>
    <a class="pill dark" href="#" style="left:833px;top:971px;width:59px">contact</a>
    <a class="pill" href="#" style="left:904px;top:971px;width:59px">quote</a>
  </aside>

  <footer class="footer">
    <nav class="footer-nav">
      <a href="#" style="left:218px">ABOUT US</a>
      <i style="left:305px"></i>
      <a href="#" style="left:332px">RESIDENTIAL</a>
      <i style="left:429px"></i>
      <a href="#" style="left:457px">COMMERCIAL</a>
      <i style="left:552px"></i>
      <a href="#" style="left:580px">REAL ESTATE/STRATA</a>
      <i style="left:719px"></i>
      <a href="#" style="left:748px">CONTACT US/QUOTE</a>
      <i style="left:882px"></i>
      <a href="#" style="left:915px">BLOG</a>
    </nav>
  </footer>
</body>
</html>
```